Flyer für Reifen- und Autoservicebetrieb
Zielgruppe
Wir sind ein Reifen- und Autoservicebetrieb; eine freie KFZ-Meister-Werkstatt ohne Markenbindung.
Aufgabenstellung
Im Focus des Flyers soll auf der Vorderseite der Reifenservice stehen, da dieser zur bevorstehenden Winterreifen-Wechselsaison erscheinen wird (Reifenwechsel, Einlagerung, Räderwäsche, Online-Termin). Auf der Rückseite soll der Autoservice und der 'neu' angebotene LKW- und Landwirtschafts- Reifenservice beworben werden.

```html
<!DOCTYPE html>
<html lang="de">
<head>
<meta charset="utf-8">
<title>Vantaro Reifen – Flyer</title>
<link rel="stylesheet" href="https://fonts.googleapis.com/css2?family=Exo+2:wght@300;400;600;700&family=Kaushan+Script&display=swap">
<style>
:root{
  --orange:#f2a21d;
  --ink:#2f2d2e;
  --grey:#d3d3d3;
  --grey-light:#e2e3e5;
  --white:#ffffff;
  --photo-light:#e9eaec;
  --photo-mid:#a9abae;
  --photo-dark:#4a4c50;
  --garage-blue:#3a5fb0;
}
*{margin:0;padding:0;box-sizing:border-box}
html,body{width:1200px;height:3200px;overflow:hidden;background:var(--white)}
body{font-family:"Exo 2",sans-serif;color:var(--ink)}
.stage{position:absolute;left:0;top:0;width:980px;height:2613px;transform:scale(1.2245);transform-origin:0 0}
.page{position:absolute;left:98px;width:788px;background:var(--grey);overflow:hidden;box-shadow:0 6px 22px rgba(0,0,0,.28)}
.page--front{top:108px;height:1114px}
.page--back{top:1353px;height:1110px}
.photo{position:absolute;left:0;top:0;width:788px}
.photo--tyre{height:500px;background:linear-gradient(90deg,var(--photo-light) 0%,var(--photo-mid) 35%,var(--photo-dark) 50%,var(--photo-mid) 65%,var(--photo-light) 100%)}
.photo--garage{height:417px;clip-path:polygon(0 0,100% 0,100% 392px,50% 417px,0 392px);background:linear-gradient(180deg,#f4f5f7 0%,#c9ced6 35%,var(--garage-blue) 62%,#9aa0a8 85%,#5a5d62 100%)}
.brand{position:absolute;left:0;width:100%;text-align:center;font-weight:700;font-size:36px;letter-spacing:1px;color:var(--orange);text-transform:uppercase}
.page--front .brand{top:60px}
.page--back .brand{top:55px}
.headline-band{position:absolute;left:0;top:467px;width:788px;height:182px;background:var(--orange);clip-path:polygon(0 0,50% 25px,100% 0,100% 155px,50% 182px,0 155px)}
.headline{position:absolute;left:0;top:512px;width:100%;text-align:center;font-weight:700;font-size:49px;line-height:53px;letter-spacing:-.5px;color:var(--ink)}
.pill{position:absolute;background:var(--ink);color:var(--white);font-weight:600;text-align:center;border-radius:24px}
.pill--tyres{left:141px;top:673px;width:512px;height:48px;line-height:48px;font-size:20px}
.pill--car{left:253px;top:450px;width:290px;height:35px;line-height:35px;font-size:21px}
.pill--new{left:347px;top:675px;width:102px;height:36px;line-height:36px;font-size:18px;background:var(--orange)}
.service-list{position:absolute;left:0;width:100%;list-style:none;text-align:center;font-weight:400;font-size:20px;line-height:28.2px}
.service-list--tyres{top:731px}
.service-list--car{top:498px}
.booking{position:absolute;left:0;top:1042px;width:100%;text-align:center}
.booking__label{font-weight:700;font-size:19px;line-height:26px}
.booking__url{font-weight:400;font-size:17px;letter-spacing:7px;line-height:26px}
.new-offer{position:absolute;left:0;top:722px;width:100%;text-align:center;font-size:20px;line-height:28px}
.contact-band{position:absolute;left:0;top:790px;width:788px;height:320px;background:var(--grey-light);clip-path:polygon(0 0,50% 25px,100% 0,100% 100%,0 100%)}
.vehicle-arc{position:absolute;left:0;top:820px;width:788px;height:90px}
.vehicle-arc text{font-family:"Kaushan Script",cursive;font-size:27px;fill:var(--ink)}
.hours{position:absolute;left:0;top:890px;width:100%;text-align:center}
.hours__title{font-weight:600;font-size:19px;line-height:26px}
.spaced{font-weight:400;font-size:18px;letter-spacing:4px;line-height:22.5px}
.address{position:absolute;left:0;top:1003px;width:100%;text-align:center}
</style>
</head>
<body>
<div class="stage">

  <section class="page page--front">
    <div class="photo photo--tyre" role="img" aria-label="Foto: Mechaniker in Handschuhen hält einen Winterreifen zwischen zwei Autos in der Werkstatt"></div>
    <div class="brand">Vantaro Reifen</div>
    <div class="headline-band"></div>
    <h1 class="headline">Ihr Experte für hochwertige<br>Reifen und Service</h1>
    <div class="pill pill--tyres">Wartung und Pflege für IhrE Räder und Reifen</div>
    <ul class="service-list service-list--tyres">
      <li>- Winterreifen</li>
      <li>- Rädereinlagerung</li>
      <li>- Reifenmontage</li>
      <li>- Auswuchten</li>
      <li>- Reifencheck</li>
      <li>- Reifenreparatur</li>
      <li>- Luftdruckkontrolle</li>
      <li>- Kalibrierung des Reifendruckkontrollsystems</li>
      <li>- Räderwäsche</li>
      <li>- Saisonaler Räder-/ Reifenwechsel</li>
    </ul>
    <div class="booking">
      <p class="booking__label">Online-Termin:</p>
      <p class="booking__url">www.VANTARO-REIFEN.de</p>
    </div>
  </section>

  <section class="page page--back">
    <div class="photo photo--garage" role="img" aria-label="Foto: helle Kfz-Werkstatt mit Hebebühne, angehobenem Auto und blauen Werkzeugwagen"></div>
    <div class="brand">Vantaro Reifen</div>
    <div class="pill pill--car">Unser Kfz-Service</div>
    <ul class="service-list service-list--car">
      <li>- Inspektion - Ölservice - &nbsp;Klimaservice</li>
      <li>- Fehlerdiagnose - Stossdämpfer Service</li>
      <li>- Hauptuntersuchung/ Abgasuntersuchung (HU/AU)</li>
      <li>- Bremsenservice - Wintercheck - BatTerieservice</li>
      <li>- Fahrzeugreparaturservice</li>
    </ul>
    <div class="pill pill--new">neu</div>
    <p class="new-offer">Reifenservice für LKW und<br>landwirtschaftliche Fahrzeuge</p>
    <div class="contact-band"></div>
    <svg class="vehicle-arc" viewBox="0 0 788 90" aria-hidden="false">
      <path id="arc" d="M250 78 Q394 18 538 78" fill="none"/>
      <text text-anchor="middle"><textPath href="#arc" startOffset="50%">fur PKW &amp; Transporter</textPath></text>
    </svg>
    <div class="hours">
      <p class="hours__title">Öffnungszeiten</p>
      <p class="spaced">Montag - Freitag</p>
      <p class="spaced">8-12 Uhr und 12:30 - 17 Uhr</p>
    </div>
    <div class="address">
      <p class="spaced">Lindenweg 12, D-24999 Musterfeld</p>
      <p class="spaced">Tel.: 04999 310 27 50</p>
      <p class="spaced">info@vantaro-reifen.de</p>
    </div>
  </section>

</div>
</body>
</html>
```